Company or website name
- Bastien GIRARDOT
- Links to the website
- /
- Describe your company and organization and target audience
- /
- The design should have the following
- I would like a design for a cv like this : http://fernandquill.com/curriculum-vitae-pavel-ostrinsky/61827  For the logos of the software in the CV, I wish to put the quillora desk pack.    Concerning the picture of portrait one must use the image attached.  Thank you.
- Other Facts

```html
<!DOCTYPE html>
<html lang="en">
<head>
<meta charset="utf-8">
<title>Curriculum Vitae – Bastien Girardot</title>
<link rel="stylesheet" href="https://fonts.googleapis.com/css2?family=Oswald:wght@600&family=Montserrat:wght@300;400;700&family=PT+Serif&display=swap">
<style>
:root{
  --stage:#2149a0;
  --paper:#ffffff;
  --ink:#2b2b2b;
  --muted:#555;
  --blue:#1a86d0;
  --blue-light:#4fb0e8;
  --orange:#ec8322;
  --yellow:#f4c21b;
  --green:#9cc84a;
  --pink:#dc7aa0;
  --red:#d9533f;
  --teal:#2e8b57;
  --rule:#3a3a3a;
  --hair:#bdbdbd;
}
*{margin:0;padding:0;box-sizing:border-box}
html,body{width:1200px;height:860px;overflow:hidden}
body{background:var(--stage);font-family:"PT Serif",serif;color:var(--ink)}
.cv{position:absolute;left:300px;top:20px;width:600px;height:820px;background:var(--paper);overflow:hidden}
.cv > *{position:absolute}
.intro{left:215px;top:26px;width:365px;font-size:8.5px;line-height:1.45;color:var(--muted)}
.top-rule{left:215px;top:92px;width:365px;border-top:2px solid var(--rule)}
.hello{left:30px;top:88px;font-family:"Oswald",sans-serif;font-weight:600;font-size:58px;line-height:1;color:var(--orange);letter-spacing:3px}
.cv-title{left:30px;top:165px;width:370px;font-family:"Montserrat",sans-serif;font-weight:300;font-size:10px;letter-spacing:2.8px;text-transform:uppercase;color:var(--ink);white-space:nowrap;overflow:hidden}
.cv-title-rule{left:30px;top:184px;width:370px;border-top:2px solid var(--rule)}
.divider{border-left:1px solid var(--hair)}
.heading{font-family:"Montserrat",sans-serif;font-weight:700;font-size:11.5px;color:var(--blue);text-transform:uppercase}
.portrait{left:40px;top:198px;width:168px;height:190px;background:radial-gradient(ellipse at 50% 40%,#9a9a9a 0%,#4a4a4a 55%,#151515 100%)}
/* artistic skills */
.skills{left:222px;top:196px;width:176px}
.skill{margin-top:6px}
.skill span{display:block;font-size:7.5px;color:var(--muted);margin-bottom:2px}
.bar{height:9px;border-radius:5px;background:linear-gradient(90deg,var(--blue),var(--blue-light))}
/* software */
.software{left:222px;top:410px;width:176px}
.apps{display:grid;grid-template-columns:repeat(3,1fr);row-gap:8px;margin-top:10px}
.app{display:flex;flex-direction:column;align-items:center;font-family:"Montserrat",sans-serif;font-size:6.5px;color:var(--muted)}
.app i{width:32px;height:32px;border-radius:50%;border:3px solid #e9eef3;margin-bottom:3px}
.suite{font-family:"Montserrat",sans-serif;font-size:7px;color:var(--muted);margin-top:6px;text-transform:uppercase;letter-spacing:1px}
.admin{left:222px;top:556px;width:176px}
.body-text{font-size:7.8px;line-height:1.45;color:var(--muted);margin-top:5px}
.travels{left:222px;top:636px;width:176px}
.trip{display:flex;gap:7px;margin-top:9px}
.date-box{flex:none;width:26px;height:26px;background:var(--blue);color:#fff;font-family:"Montserrat",sans-serif;font-size:7px;font-weight:700;text-align:center;line-height:1.15;padding-top:3px}
.trip h4,.school h4{font-family:"Montserrat",sans-serif;font-size:8.5px;font-weight:700;text-transform:uppercase;color:var(--ink)}
.place{font-family:"Montserrat",sans-serif;font-size:7px;color:var(--orange);text-transform:uppercase}
/* education */
.education{left:40px;top:410px;width:168px}
.school{position:relative;margin-top:10px;padding-right:24px}
.school .year{position:absolute;right:0;top:0;width:18px;height:18px;background:var(--yellow);color:#fff;font-family:"Montserrat",sans-serif;font-size:8px;font-weight:700;text-align:center;line-height:18px}
/* right column */
.language{left:416px;top:108px;width:166px}
.donuts{display:flex;justify-content:space-between;margin-top:8px}
.donut{display:flex;flex-direction:column;align-items:center;font-size:6.5px;color:var(--muted);text-transform:uppercase}
.donut svg{width:44px;height:44px}
.short-rule{width:50px;border-top:1.5px solid var(--hair)}
.interests{left:416px;top:232px;width:166px}
.interest{display:flex;align-items:center;gap:12px;margin-top:11px;font-family:"Montserrat",sans-serif;font-size:7px;text-transform:uppercase;color:var(--ink)}
.interest svg{width:24px;height:22px;flex:none}
.contacts{left:416px;top:460px;width:166px}
.contact{display:flex;align-items:center;gap:14px;margin-top:10px;font-family:"Montserrat",sans-serif;font-size:8px;color:var(--ink)}
.contact .dot{flex:none;width:16px;height:16px;border-radius:50%;background:var(--blue);display:flex;align-items:center;justify-content:center}
.contact .dot svg{width:9px;height:9px}
.foot-band{left:0;bottom:0;width:600px;height:7px;background:var(--orange)}
</style>
</head>
<body>
<main class="cv">
  <p class="intro">Lorem Ipsum is simply dummy text of the printing and typesetting industry. Lorem Ipsum has been the industry's standard dummy text ever since the 1500s, when an unknown printer took a galley of type and scrambled it to make a type specimen book. It has survived not only five centuries, but also the leap into electronic typesetting, remaining essentially unchanged.</p>
  <div class="top-rule"></div>
  <h1 class="hello">HELLO!</h1>
  <h2 class="cv-title">Curriculum Vitae of Bastien Girardot</h2>
  <div class="cv-title-rule"></div>

  <div class="divider" style="left:405px;top:104px;height:690px"></div>
  <div class="divider" style="left:214px;top:400px;height:394px"></div>

  <div class="portrait" role="img" aria-label="Black and white portrait photograph of Bastien Girardot"></div>

  <section class="skills">
    <h3 class="heading">Artistic Skills</h3>
    <div class="skill"><span>Administration</span><div class="bar" style="width:100%"></div></div>
    <div class="skill"><span>Presentation</span><div class="bar" style="width:92%"></div></div>
    <div class="skill"><span>Accounts</span><div class="bar" style="width:86%"></div></div>
    <div class="skill"><span>Administration</span><div class="bar" style="width:96%"></div></div>
    <div class="skill"><span>Presentation</span><div class="bar" style="width:80%"></div></div>
    <div class="skill"><span>Accounts</span><div class="bar" style="width:74%"></div></div>
  </section>

  <section class="software">
    <h3 class="heading">Software Skills</h3>
    <div class="apps">
      <div class="app"><i style="background:#2b5fb4"></i>Write</div>
      <div class="app"><i style="background:var(--red)"></i>Slides</div>
      <div class="app"><i style="background:var(--teal)"></i>Sheets</div>
      <div class="app"><i style="background:#2b5fb4"></i>Mail</div>
      <div class="app"><i style="background:#c8453b"></i>Base</div>
      <div class="app"><i style="background:#1a86d0"></i>Notes</div>
    </div>
    <p class="suite">quillora desk</p>
  </section>

  <section class="admin">
    <h3 class="heading">Admin Fields</h3>
    <p class="body-text">Lorem Ipsum is simply dummy text of the printing and typesetting industry. Lorem Ipsum has been the industry's standard dummy text.</p>
  </section>

  <section class="travels">
    <h3 class="heading">Travels</h3>
    <div class="trip">
      <div class="date-box">JAN<br>2016</div>
      <div><h4>Lorem Ipsum is simply</h4><p class="place">France</p><p class="body-text">Lorem Ipsum is simply dummy text of the printing and typesetting industry.</p></div>
    </div>
    <div class="trip">
      <div class="date-box">MAR<br>2017</div>
      <div><h4>Lorem Ipsum is simply</h4><p class="place">United Kingdom</p><p class="body-text">Lorem Ipsum is simply dummy text of the printing and typesetting industry.</p></div>
    </div>
  </section>

  <section class="education">
    <h3 class="heading">Education</h3>
    <div class="school">
      <span class="year">05</span>
      <h4>University of USA</h4>
      <p class="place" style="text-transform:none">Bachelor in Administration</p>
      <p class="body-text">Lorem Ipsum is simply dummy text of the printing and typesetting industry. Lorem Ipsum has been the industry's standard dummy text.</p>
    </div>
    <div class="school">
      <span class="year">10</span>
      <h4>University of USA</h4>
      <p class="place" style="text-transform:none">Master in Administration</p>
      <p class="body-text">Lorem Ipsum is simply dummy text of the printing and typesetting industry. Lorem Ipsum has been the industry's standard dummy text.</p>
    </div>
  </section>

  <section class="language">
    <h3 class="heading">Language</h3>
    <div class="donuts">
      <div class="donut">
        <svg viewBox="0 0 44 44"><circle cx="22" cy="22" r="17" fill="none" stroke="#e4eef7" stroke-width="5"/><circle cx="22" cy="22" r="17" fill="none" stroke="var(--blue)" stroke-width="5" stroke-dasharray="105.7 106.8" transform="rotate(-90 22 22)"/><text x="22" y="25" text-anchor="middle" font-family="Montserrat,sans-serif" font-size="8" font-weight="700" fill="#2b2b2b">99%</text></svg>
        English
      </div>
      <div class="donut">
        <svg viewBox="0 0 44 44"><circle cx="22" cy="22" r="17" fill="none" stroke="#dfeccb" stroke-width="5"/><circle cx="22" cy="22" r="17" fill="none" stroke="var(--green)" stroke-width="5" stroke-dasharray="21.4 106.8" transform="rotate(-90 22 22)"/><text x="22" y="25" text-anchor="middle" font-family="Montserrat,sans-serif" font-size="8" font-weight="700" fill="#2b2b2b">20%</text></svg>
        German
      </div>
      <div class="donut">
        <svg viewBox="0 0 44 44"><circle cx="22" cy="22" r="17" fill="none" stroke="#f5d9e4" stroke-width="5"/><circle cx="22" cy="22" r="17" fill="none" stroke="var(--pink)" stroke-width="5" stroke-dasharray="49.1 106.8" transform="rotate(-90 22 22)"/><text x="22" y="25" text-anchor="middle" font-family="Montserrat,sans-serif" font-size="8" font-weight="700" fill="#2b2b2b">46%</text></svg>
        Spanish
      </div>
    </div>
    <div class="short-rule" style="margin:22px 0 0 30px"></div>
  </section>

  <section class="interests">
    <h3 class="heading">Interests</h3>
    <div class="interest"><svg viewBox="0 0 24 22"><ellipse cx="12" cy="7" rx="10" ry="4" fill="var(--blue)"/><rect x="2" y="7" width="20" height="10" fill="var(--blue)"/><ellipse cx="12" cy="17" rx="10" ry="4" fill="var(--blue)"/><ellipse cx="12" cy="7" rx="8" ry="2.5" fill="#fff"/></svg><span>Music<br>Playing drum</span></div>
    <div class="interest"><svg viewBox="0 0 24 22"><path d="M3 12l7-1 5-8h3l-3 8 5 0 2-3h2l-1 4 1 4h-2l-2-3h-5l3 8h-3l-5-8-7-1z" fill="var(--blue)"/></svg><span>Traveling</span></div>
    <div class="interest"><svg viewBox="0 0 24 22"><rect x="2" y="6" width="20" height="13" rx="2" fill="var(--blue)"/><rect x="8" y="3" width="8" height="4" fill="var(--blue)"/><circle cx="12" cy="12.5" r="4" fill="#fff"/></svg><span>Photography</span></div>
    <div class="interest"><svg viewBox="0 0 24 22"><rect x="2" y="3" width="20" height="16" fill="var(--blue)"/><path d="M10 7l6 4-6 4z" fill="#fff"/></svg><span>Movies</span></div>
    <div class="interest"><svg viewBox="0 0 24 22"><ellipse cx="12" cy="11" rx="10" ry="6" transform="rotate(-30 12 11)" fill="var(--blue)"/><path d="M8 13l8-4" stroke="#fff" stroke-width="1.2"/></svg><span>Sports<br>Playing football</span></div>
    <div class="short-rule" style="margin:18px 0 0 30px"></div>
  </section>

  <section class="contacts">
    <h3 class="heading">Contacts</h3>
    <div class="contact"><span class="dot"><svg viewBox="0 0 10 10"><path d="M2 1l2 2-1 1.5c.6 1.2 1.3 1.9 2.5 2.5L7 6l2 2-1.5 1.5C4 9 1 6 .5 2.5z" fill="#fff"/></svg></span>555 013 247</div>
    <div class="contact"><span class="dot"><svg viewBox="0 0 10 10"><circle cx="5" cy="5" r="4" fill="none" stroke="#fff"/><path d="M1 5h8M5 1c-2 2.5-2 5.5 0 8M5 1c2 2.5 2 5.5 0 8" stroke="#fff" fill="none" stroke-width=".8"/></svg></span>www.bgirardot.net</div>
    <div class="contact"><span class="dot"><svg viewBox="0 0 10 10"><rect x="1" y="2.5" width="8" height="5.5" fill="#fff"/><path d="M1 2.5l4 3 4-3" stroke="var(--blue)" fill="none" stroke-width=".8"/></svg></span>hello@bgirardot.net</div>
    <div class="contact"><span class="dot"></span>social.net/bgirardot</div>
    <div class="contact"><span class="dot"></span>bastien.girardot</div>
    <div class="contact"><span class="dot"></span>555 013 247</div>
  </section>

  <div class="foot-band"></div>
</main>
</body>
</html>
```